Template design for an Online "Membership Subscription" System

I need a template for a service that will allow website owners to create their own online subscription services and member portals.
With just a snippet of code they can password protect certain parts of their website.
Tagline:
"Monetize your website with TallyGateClubs"
"The Easiest Way To Turn Your Website Into 'Members Only'"
Call to action "Try For Free" and "Watch a demo"
Features:
1. Quick & easy to set up
2. Works with any website
3. Charge one-time or subscription fees
4. Automated billing, sign up and more
5. Customize to match your website
6. Unlimited members
Similar websites/services;
https://lockvaultsuite.example
https://joinrova.example
https://www.guildnook.example
I'd like a clean looking, uncluttered design targeted towards "non-techie" people. Easy to read without a lot going on. Emphasizing ease of use and pushing towards a "Try for free" option.
Separate into sections with the top section having the tagline. Followed by feature overview, testimonials, sample use cases.
A footer with multiple links by industry that can provide a case study for various use cases;
Ex;
Clubs
Religious Organizations
Online Stores
Digital Products
Education
Coaching
Fitness
Target Market(s)
Non technical small business owners
Number of Pages Required
2 page
Look and feel
Each slider illustrates characteristics of the customer's brand and the style your logo design should communicate.

```html
<!DOCTYPE html>
<html lang="en">
<head>
<meta charset="utf-8">
<title>Members Only Made Easy</title>
<link href="https://fonts.googleapis.com/css2?family=Archivo:wght@400;500;600;700;800;900&family=Roboto:wght@400;500;700&display=swap" rel="stylesheet">
<style>
:root{
  --blue:#0b63ce;
  --blue-deep:#0a47a3;
  --ink:#111418;
  --muted:#4a5260;
  --pale:#eaf2fc;
  --hero-bg:#f2f6fc;
  --footer:#1f2226;
  --white:#ffffff;
}
*{margin:0;padding:0;box-sizing:border-box}
html,body{width:1200px;height:3940px;overflow:hidden}
body{position:relative;background:var(--white);font-family:"Roboto",sans-serif;color:var(--ink)}
.abs{position:absolute}
.btn{position:absolute;display:flex;align-items:center;justify-content:center;font-family:"Archivo",sans-serif;font-weight:700;font-size:13px;letter-spacing:.3px;text-transform:uppercase;border-radius:3px;text-decoration:none}
.btn-solid{background:var(--blue);color:var(--white)}
.btn-outline{border:2px solid var(--blue);color:var(--blue);background:var(--white)}
h2.section-title{position:absolute;left:0;width:1200px;text-align:center;font-family:"Archivo",sans-serif;font-weight:800;font-size:38px;letter-spacing:.5px}

/* header + hero */
.hero{position:absolute;left:0;top:0;width:1200px;height:720px;overflow:hidden}
.hero-bg{position:absolute;inset:0}
.logo{left:112px;top:44px;font-family:"Archivo",sans-serif;font-weight:700;font-size:34px;color:var(--ink)}
.nav a{position:absolute;top:56px;font-family:"Archivo",sans-serif;font-size:14px;font-weight:500;color:var(--ink);text-decoration:none}
.hero-art{left:650px;top:0;width:530px;height:600px;border-radius:0 0 0 40px;background:linear-gradient(160deg,#dfeafb 0%,#c6dbf7 55%,#eaf2fc 100%)}
.hero-title{left:112px;top:258px;font-family:"Archivo",sans-serif;font-weight:800;font-size:54px;line-height:60px;color:var(--ink);width:780px}

/* features */
.feature{position:absolute;width:308px;height:320px;border:2px solid var(--blue);border-radius:8px;background:var(--pale);text-align:center;padding:0 30px;box-shadow:0 4px 12px rgba(11,99,206,.12)}
.feature.is-active{background:linear-gradient(160deg,#0b6ad8,#0a47a3);color:var(--white)}
.feature .icon{width:88px;height:88px;margin:48px auto 0;border-radius:50%;background:var(--blue);display:flex;align-items:center;justify-content:center}
.feature.is-active .icon{background:var(--white)}
.feature h3{margin-top:30px;font-family:"Archivo",sans-serif;font-weight:800;font-size:15px;line-height:20px;text-transform:uppercase}
.feature p{margin-top:12px;font-size:13px;line-height:18px;color:var(--muted)}
.feature.is-active p{color:#e4eefc}

/* testimonials */
.testimonials{position:absolute;left:0;top:1668px;width:1200px;height:520px;background:linear-gradient(135deg,#0b72e0 0%,#0a5cc8 50%,#0a44a6 100%);color:var(--white)}
.testimonials h2{position:absolute;top:106px;width:1200px;text-align:center;font-family:"Archivo",sans-serif;font-weight:800;font-size:38px}
.quote{position:absolute;top:196px;width:270px;text-align:center}
.quote .mark{font-family:"Archivo",sans-serif;font-weight:900;font-size:64px;line-height:40px;height:40px}
.quote p{margin-top:18px;font-size:14px;line-height:18px;font-weight:500}
.quote .who{margin-top:10px;font-weight:700;font-size:14px}
.dots{position:absolute;top:410px;left:576px;display:flex;gap:10px}
.dots span{width:8px;height:8px;border-radius:50%;background:rgba(255,255,255,.5)}
.dots span:first-child{background:var(--white)}

/* how it works */
.how-intro{position:absolute;left:140px;top:2350px;width:920px;text-align:center;font-size:14px;line-height:20px;color:var(--muted)}
.step{position:absolute;top:2420px;width:272px;height:330px;background:var(--white);box-shadow:0 6px 20px rgba(10,30,70,.14);border-bottom:5px solid var(--blue-deep);padding:0 32px}
.step .icon{width:110px;height:110px;margin:32px auto 0;border-radius:50%;background:radial-gradient(circle at 40% 35%,#1a7ae6,#0a3f95);display:flex;align-items:center;justify-content:center}
.step h3{margin-top:28px;font-family:"Archivo",sans-serif;font-weight:800;font-size:18px}
.step p{margin-top:10px;font-size:14px;line-height:20px;color:var(--muted)}

/* contact */
.contact{position:absolute;left:0;top:2850px;width:1200px;height:530px;background:linear-gradient(180deg,#f2f6fc,#e8eff9)}
.contact h2{position:absolute;top:70px;width:1200px;text-align:center;font-family:"Archivo",sans-serif;font-weight:800;font-size:38px}
.addr-title{left:200px;top:176px;font-family:"Archivo",sans-serif;font-weight:800;font-size:20px}
.addr-item{position:absolute;left:200px;display:flex;align-items:center;gap:16px;font-size:13px;line-height:18px;color:var(--muted)}
.addr-item .dot{width:34px;height:34px;border-radius:50%;background:var(--blue);display:flex;align-items:center;justify-content:center;flex:none}
.social{position:absolute;left:200px;top:400px;display:flex;gap:16px}
.social span{width:36px;height:36px;border-radius:50%;background:var(--blue)}
.field{position:absolute;height:40px;background:var(--white);border:1px solid #c9d6ea;font-size:12px;color:#7a8494;padding:12px 14px}
.submit{left:880px;top:380px;width:120px;height:40px}

/* footer */
.footer{position:absolute;left:0;top:3380px;width:1200px;height:560px;background:var(--footer);color:var(--white)}
.foot-col{position:absolute;width:230px}
.foot-col h4{font-family:"Archivo",sans-serif;font-weight:700;font-size:20px;text-decoration:underline;text-underline-offset:5px;margin-bottom:14px}
.foot-col li{list-style:none;font-size:15px;line-height:28px}
.copyright{position:absolute;top:512px;width:1200px;text-align:center;font-size:13px}
</style>
</head>
<body>

<section class="hero">
  <svg class="hero-bg" width="1200" height="720" viewBox="0 0 1200 720" aria-hidden="true">
    <path d="M0 0H1200V610C1020 700 820 650 640 660C420 672 200 720 0 690Z" fill="var(--hero-bg)"/>
  </svg>
  <div class="hero-art abs" role="img" aria-label="Isometric illustration of a website page being locked behind a member login, with gears and a shield"></div>
  <div class="logo abs">COMPANY LOGO</div>
  <nav class="nav">
    <a style="left:494px">Home</a>
    <a style="left:580px">Pricing</a>
    <a style="left:676px">Services</a>
    <a style="left:774px">Support</a>
  </nav>
  <a class="btn btn-outline" style="left:860px;top:46px;width:86px;height:36px">Sign Up</a>
  <a class="btn btn-solid" style="left:964px;top:46px;width:128px;height:36px">Try For Free</a>
  <h1 class="hero-title abs">The Easiest Way To<br>Turn Your Website Into<br>'Members Only</h1>
  <a class="btn btn-outline" style="left:112px;top:470px;width:128px;height:40px">Watch A Demo</a>
  <a class="btn btn-solid" style="left:268px;top:470px;width:112px;height:40px">Try For Free</a>
</section>

<h2 class="section-title" style="top:752px">OUR FEATURES</h2>

<article class="feature" style="left:112px;top:840px">
  <div class="icon"><svg width="44" height="44" viewBox="0 0 44 44" fill="none" stroke="#fff" stroke-width="3"><circle cx="17" cy="20" r="7"/><circle cx="17" cy="20" r="12" stroke-dasharray="5 4"/><circle cx="32" cy="31" r="5"/></svg></div>
  <h3>Quick &amp; Easy To Set Up<br>And Work</h3>
  <p>Lorem ipsum dolor sit amet, consectetur adipiscing elit, sed do eiusmod tempor incididunt ut labore et dolore magna aliqua.</p>
</article>
<article class="feature is-active" style="left:444px;top:840px">
  <div class="icon"><svg width="44" height="44" viewBox="0 0 44 44" fill="none" stroke="#0b63ce" stroke-width="3"><rect x="6" y="10" width="32" height="22" rx="2"/><path d="M16 38H28M22 32V38"/></svg></div>
  <h3>Works With Any Website</h3>
  <p>Lorem ipsum dolor sit amet, consectetur adipiscing elit, sed do eiusmod tempor incididunt ut labore et dolore magna aliqua.</p>
</article>
<article class="feature" style="left:780px;top:840px">
  <div class="icon"><svg width="44" height="44" viewBox="0 0 44 44" fill="none" stroke="#fff" stroke-width="3"><circle cx="22" cy="22" r="13"/><path d="M26 16H20a3 3 0 0 0 0 6h4a3 3 0 0 1 0 6H17M22 12V32"/></svg></div>
  <h3>Charge One-Time Or<br>Subscription Fees</h3>
  <p>Lorem ipsum dolor sit amet, consectetur adipiscing elit, sed do eiusmod tempor incididunt ut labore et dolore magna aliqua.</p>
</article>
<article class="feature" style="left:112px;top:1190px">
  <div class="icon"><svg width="44" height="44" viewBox="0 0 44 44" fill="none" stroke="#fff" stroke-width="3"><rect x="10" y="6" width="24" height="32" rx="2"/><path d="M15 14H29M15 20H29M15 26H23"/></svg></div>
  <h3>Automated Billing, Sign Up<br>And More</h3>
  <p>Lorem ipsum dolor sit amet, consectetur adipiscing elit, sed do eiusmod tempor incididunt ut labore et dolore magna aliqua.</p>
</article>
<article class="feature" style="left:444px;top:1190px">
  <div class="icon"><svg width="44" height="44" viewBox="0 0 44 44" fill="none" stroke="#fff" stroke-width="3"><rect x="7" y="7" width="30" height="30" rx="3"/><circle cx="22" cy="22" r="7"/></svg></div>
  <h3>Customize To Match Your Website</h3>
  <p>Lorem ipsum dolor sit amet, consectetur adipiscing elit, sed do eiusmod tempor incididunt ut labore et dolore magna aliqua.</p>
</article>
<article class="feature" style="left:780px;top:1190px">
  <div class="icon"><svg width="44" height="44" viewBox="0 0 44 44" fill="none" stroke="#fff" stroke-width="3"><circle cx="16" cy="16" r="5"/><circle cx="29" cy="16" r="5"/><path d="M7 33c0-6 4-9 9-9s9 3 9 9M21 27c2-2 4-3 8-3 5 0 9 3 9 9"/></svg></div>
  <h3>Unlimited Members</h3>
  <p>Lorem ipsum dolor sit amet, consectetur adipiscing elit, sed do eiusmod tempor incididunt ut labore et dolore magna aliqua.</p>
</article>

<a class="btn btn-outline" style="left:460px;top:1556px;width:130px;height:40px">Get Started</a>
<a class="btn btn-solid" style="left:618px;top:1556px;width:130px;height:40px">Try For Free</a>

<section class="testimonials">
  <h2>TESTIMONIALS</h2>
  <blockquote class="quote" style="left:165px">
    <div class="mark">&ldquo;</div>
    <p>Lorem ipsum dolor sit amet, consectetur adipiscing elit, sed do eiusmod tempor incididunt ut labore et dolore magna aliqua. Quis ipsum suspendisse.</p>
    <div class="who">- Daniel Whitford</div>
  </blockquote>
  <blockquote class="quote" style="left:465px">
    <div class="mark">&ldquo;</div>
    <p>Lorem ipsum dolor sit amet, consectetur adipiscing elit, sed do eiusmod tempor incididunt ut labore et dolore magna aliqua. Quis ipsum suspendisse.</p>
    <div class="who">- Daniel Whitford</div>
  </blockquote>
  <blockquote class="quote" style="left:765px">
    <div class="mark">&ldquo;</div>
    <p>Lorem ipsum dolor sit amet, consectetur adipiscing elit, sed do eiusmod tempor incididunt ut labore et dolore magna aliqua. Quis ipsum suspendisse.</p>
    <div class="who">- Daniel Whitford</div>
  </blockquote>
  <div class="dots"><span></span><span></span><span></span></div>
</section>

<h2 class="section-title" style="top:2290px">HOW IT WORKS</h2>
<p class="how-intro">Lorem ipsum dolor sit amet, consectetur adipiscing elit, sed do eiusmod tempor incididunt ut labore et dolore magna aliqua. Quis ipsum suspendisse ultrices gravida.</p>

<article class="step" style="left:152px">
  <div class="icon"><svg width="50" height="50" viewBox="0 0 56 56" fill="none" stroke="#fff" stroke-width="3"><path d="M12 44L36 20M30 14l12 12M14 14l28 28"/></svg></div>
  <h3>Lorem Ipsum</h3>
  <p>Lorem ipsum dolor sit amet, cons ectetur adipiscing elit, sed do eiusmod tempor incididunt ut labore et dolore aliqua. Quis ipsum.</p>
</article>
<article class="step" style="left:464px">
  <div class="icon"><svg width="50" height="50" viewBox="0 0 56 56" fill="none" stroke="#fff" stroke-width="3"><rect x="18" y="8" width="20" height="40" rx="3"/><path d="M6 22l6 6-6 6M50 22l-6 6 6 6"/></svg></div>
  <h3>Lorem Ipsum</h3>
  <p>Lorem ipsum dolor sit amet, cons ectetur adipiscing elit, sed do eiusmod tempor incididunt ut labore et dolore aliqua. Quis ipsum.</p>
</article>
<article class="step" style="left:776px">
  <div class="icon"><svg width="50" height="50" viewBox="0 0 56 56" fill="none" stroke="#fff" stroke-width="3"><circle cx="24" cy="18" r="8"/><path d="M10 46c0-9 6-14 14-14"/><rect x="32" y="34" width="16" height="12" rx="2"/><path d="M35 34v-4a5 5 0 0 1 10 0v4"/></svg></div>
  <h3>Lorem Ipsum</h3>
  <p>Lorem ipsum dolor sit amet, cons ectetur adipiscing elit, sed do eiusmod tempor incididunt ut labore et dolore aliqua. Quis ipsum.</p>
</article>

<section class="contact">
  <h2>GET IN TOUCH WITH US</h2>
  <div class="addr-title abs">ADDRESS</div>
  <div class="addr-item" style="top:228px"><span class="dot"><svg width="16" height="16" viewBox="0 0 16 16" fill="#fff"><path d="M8 1a5 5 0 0 0-5 5c0 4 5 9 5 9s5-5 5-9a5 5 0 0 0-5-5zm0 7a2 2 0 1 1 0-4 2 2 0 0 1 0 4z"/></svg></span><span>18 Harbor Lane, Maple Row,<br>Brookfield 456</span></div>
  <div class="addr-item" style="top:284px"><span class="dot"><svg width="16" height="16" viewBox="0 0 16 16" fill="#fff"><path d="M4 1l3 3-2 2c1 2 3 4 5 5l2-2 3 3-2 3C7 15 1 9 1 3z"/></svg></span><span>Phone Number<br>+1 111 1111 111</span></div>
  <div class="addr-item" style="top:340px"><span class="dot"><svg width="16" height="16" viewBox="0 0 16 16" fill="none" stroke="#fff" stroke-width="1.6"><rect x="1.5" y="3.5" width="13" height="9"/><path d="M2 4l6 5 6-5"/></svg></span><span>Email Address<br>info@postmail.example</span></div>
  <div class="social" aria-label="Social links"><span></span><span></span><span></span><span></span></div>

  <div class="field" style="left:530px;top:170px;width:220px">First Name</div>
  <div class="field" style="left:780px;top:170px;width:220px">Last Name</div>
  <div class="field" style="left:530px;top:226px;width:220px">Contact Number</div>
  <div class="field" style="left:780px;top:226px;width:220px">Email Address</div>
  <div class="field" style="left:530px;top:282px;width:470px;height:80px">Message Goes Here...</div>
  <a class="btn btn-solid submit">Submit Now</a>
</section>

<footer class="footer">
  <div class="foot-col" style="left:192px;top:104px"><h4>Clubs</h4><ul><li>Link Name 1</li><li>Link Name 2</li><li>Link Name 3</li><li>Link Name 4</li></ul></div>
  <div class="foot-col" style="left:392px;top:104px"><h4>Online Stores</h4><ul><li>Link Name 1</li><li>Link Name 2</li><li>Link Name 3</li><li>Link Name 4</li></ul></div>
  <div class="foot-col" style="left:640px;top:104px"><h4>Digital Products</h4><ul><li>Link Name 1</li><li>Link Name 2</li><li>Link Name 3</li><li>Link Name 4</li></ul></div>
  <div class="foot-col" style="left:912px;top:104px"><h4>Fitness</h4><ul><li>Link Name 1</li><li>Link Name 2</li><li>Link Name 3</li></ul></div>
  <div class="foot-col" style="left:192px;top:318px"><h4>Education</h4><ul><li>Link Name 1</li><li>Link Name 2</li><li>Link Name 3</li><li>Link Name 4</li></ul></div>
  <div class="foot-col" style="left:392px;top:318px"><h4>Coaching</h4><ul><li>Link Name 1</li><li>Link Name 2</li><li>Link Name 3</li><li>Link Name 4</li></ul></div>
  <div class="foot-col" style="left:640px;top:318px;width:300px"><h4>Religious Organizations</h4><ul><li>Link Name 1</li><li>Link Name 2</li><li>Link Name 3</li><li>Link Name 4</li></ul></div>
  <p class="copyright">&copy; 2022 Website Name | All Rights Reserved.</p>
</footer>

</body>
</html>
```